Lumex

Hello Artboardly Community,

Thank you for participating in designing Snapquill App. So far I've received some amazing looking designs!
Unfortunately, Some of the designs being submitted are not following the project brief.
The screens you submit should be designed "1:1 / Exactly" according to the project brief.
Updates

Target Market(s)

Millennials

Industry/Entity Type

Community

Font styles to use
Sans Serif

Requirements
Must have
• Follow the project brief exactly.

```html
<!DOCTYPE html>
<html lang="en">
<head>
<meta charset="utf-8">
<title>Snapquill – App Screens</title>
<link href="https://fonts.googleapis.com/css2?family=Montserrat:wght@300;400;500;600;700&family=Open+Sans:wght@400&family=Libre+Baskerville&display=swap" rel="stylesheet">
<style>
  :root{
    --stage:#272727;
    --camera-grey:#898989;
    --white:#ffffff;
    --ink:#2b2b2b;
    --muted:#555555;
    --icon:#8a8a8a;
    --grid-bg:#ececec;
    --accent-green:#8fd14f;
    --forest-dark:#1f3a30;
    --forest-mid:#3d5a4c;
  }
  *{box-sizing:border-box;margin:0;padding:0}
  html,body{width:1200px;height:1000px;overflow:hidden}
  body{background:var(--stage);position:relative;font-family:"Montserrat",sans-serif}
  .screen{position:absolute;top:185px;width:354px;height:630px;overflow:hidden}
  .abs{position:absolute}

  /* Camera screen */
  .screen--camera{left:38px;background:var(--camera-grey);color:var(--white)}
  .camera__title{left:45px;top:15px;font-size:18px;font-weight:600;letter-spacing:-.2px}
  .camera__prompt{left:0;width:100%;top:274px;text-align:center;font-size:17px;font-weight:300}
  .camera__shutter{left:140px;top:536px;width:74px;height:74px;border-radius:50%;background:#d9d9d9;border:4px solid #bdbdbd;display:flex;align-items:center;justify-content:center}
  .camera__shutter-inner{width:62px;height:62px;border-radius:50%;background:var(--white);display:flex;align-items:center;justify-content:center}

  /* Files screen */
  .screen--files{left:425px;background:var(--grid-bg)}
  .appbar{position:absolute;left:0;top:0;width:100%;height:52px;background:var(--white);border-bottom:1px solid #e2e2e2}
  .appbar__label{position:absolute;top:17px;font-size:15px;color:var(--muted);font-weight:400;letter-spacing:.3px}
  .tile{position:absolute;overflow:hidden}
  .tile__art{position:absolute;inset:0}
  .tile__word{position:absolute;left:0;width:100%;text-align:center;color:var(--white)}
  .tile--sculp{left:6px;top:60px;width:167px;height:167px}
  .tile--sculp .tile__art{background:radial-gradient(circle at 50% 55%,#9a968f 0%,#6b6964 45%,#3d3c3a 100%)}
  .tile--sculp .tile__word{top:64px;font-size:26px;font-weight:300;letter-spacing:1px}
  .tile--art{left:6px;top:234px;width:167px;height:230px}
  .tile--art .tile__art{background:linear-gradient(160deg,#f7d9c2 0%,#f2a3a8 35%,#6cc3a5 60%,#f5c0a0 100%)}
  .tile--art .tile__word{top:10px;font-size:118px;font-weight:700;line-height:1;letter-spacing:-6px;opacity:.95}
  .tile--expressions{left:6px;top:471px;width:167px;height:170px;background:var(--white)}
  .tile--expressions .tile__word{top:28px;color:#111;font-size:21px;font-weight:400;letter-spacing:-.8px}
  .tile--expressions .tile__art{top:72px;left:10px;right:10px;bottom:0;background:linear-gradient(180deg,#d6d6d6,#6e6e6e)}
  .tile--oceania{left:181px;top:60px;width:167px;height:83px}
  .tile--oceania .tile__art{background:linear-gradient(180deg,#2f8fce 0%,#1a5f9a 55%,#0d3868 100%)}
  .tile--oceania .tile__word{top:31px;font-size:15px;font-weight:300;letter-spacing:5px}
  .tile--nature{left:181px;top:151px;width:167px;height:232px}
  .tile--nature .tile__art{background:linear-gradient(180deg,#f1efeb 0%,#d7ddd8 35%,#5d7c6c 65%,var(--forest-dark) 100%)}
  .tile--nature .tile__word{color:#222}
  .tile--phones{left:181px;top:390px;width:167px;height:166px}
  .tile--phones .tile__art{background:linear-gradient(135deg,#121212 0%,#2b2b2b 45%,#5f5fd9 62%,#e8e2d4 80%,#1a1a1a 100%)}
  .tile--universe{left:181px;top:563px;width:167px;height:80px;background:#f1f0ed;font-family:"Libre Baskerville",serif;color:#333}
  .fab{left:281px;top:555px;width:62px;height:62px;border-radius:50%;background:var(--white);border:3px solid #cfcfcf;display:flex;align-items:center;justify-content:center}

  /* Detail screen */
  .screen--detail{left:812px;background:#e9ebea}
  .hero{position:absolute;left:6px;top:52px;width:342px;height:248px}
  .hero__art{position:absolute;inset:0;background:linear-gradient(180deg,#2c4a3d 0%,var(--forest-mid) 40%,var(--forest-dark) 100%)}
  .title-light{font-weight:300;letter-spacing:.42em}
  .title-bold{font-weight:700;letter-spacing:.04em}
  .article{position:absolute;left:6px;top:307px;width:342px;height:330px;background:linear-gradient(180deg,#fdfdfd 0%,#f4f6f5 40%,#e2e7e4 100%)}
  .article__heading{position:absolute;left:30px;top:37px;font-size:20px;font-weight:300;color:#222}
  .article__part{position:absolute;left:32px;top:62px;font-size:11px;font-weight:600;color:#222}
  .article__body{position:absolute;left:33px;top:103px;width:290px;font-family:"Open Sans",sans-serif;font-size:11.2px;line-height:14.2px;color:#222}
  .article__body p+p{margin-top:14px}
</style>
</head>
<body>

<!-- Camera / compose screen -->
<section class="screen screen--camera">
  <svg class="abs" style="left:14px;top:19px" width="18" height="14" viewBox="0 0 18 14"><g stroke="#fff" stroke-width="2"><line x1="0" y1="1" x2="18" y2="1"/><line x1="0" y1="7" x2="18" y2="7"/><line x1="0" y1="13" x2="18" y2="13"/></g></svg>
  <div class="abs camera__title">Snapquill</div>
  <svg class="abs" style="left:320px;top:16px" width="20" height="20" viewBox="0 0 20 20" fill="none" stroke="#fff" stroke-width="1.2"><rect x="0.6" y="0.6" width="18.8" height="18.8"/><rect x="3" y="4" width="7" height="6"/><line x1="12" y1="5" x2="17" y2="5"/><line x1="12" y1="8" x2="17" y2="8"/><line x1="3" y1="13" x2="17" y2="13"/><line x1="3" y1="16" x2="17" y2="16"/></svg>
  <div class="abs camera__prompt">Type something...</div>
  <svg class="abs" style="left:54px;top:561px" width="26" height="26" viewBox="0 0 26 26" fill="none" stroke="#eee" stroke-width="1.3"><rect x="0.7" y="0.7" width="11" height="24.6"/><rect x="14.3" y="0.7" width="11" height="11"/><rect x="14.3" y="14.3" width="11" height="11"/></svg>
  <div class="abs camera__shutter"><div class="camera__shutter-inner">
    <svg width="24" height="18" viewBox="0 0 24 18" fill="none" stroke="var(--accent-green)" stroke-width="1.4"><path d="M1 4h6l2-3h6l2 3h6v13H1z"/><circle cx="12" cy="10" r="4"/></svg>
  </div></div>
  <svg class="abs" style="left:268px;top:561px" width="26" height="26" viewBox="0 0 26 26" stroke="#eee" stroke-width="1.4"><line x1="13" y1="0" x2="13" y2="26"/><line x1="0" y1="13" x2="26" y2="13"/></svg>
</section>

<!-- Files grid screen -->
<section class="screen screen--files">
  <header class="appbar">
    <svg class="abs" style="left:13px;top:20px" width="18" height="12" viewBox="0 0 18 12"><g stroke="var(--icon)" stroke-width="1.3"><line x1="0" y1="1" x2="18" y2="1"/><line x1="0" y1="6" x2="18" y2="6"/><line x1="0" y1="11" x2="18" y2="11"/></g></svg>
    <span class="appbar__label" style="left:46px">ALL FILES</span>
    <svg class="abs" style="left:135px;top:22px" width="14" height="8" viewBox="0 0 14 8" fill="none" stroke="var(--muted)" stroke-width="1.4"><path d="M1 1l6 6 6-6"/></svg>
    <svg class="abs" style="left:318px;top:15px" width="21" height="21" viewBox="0 0 21 21" fill="none" stroke="var(--icon)" stroke-width="1.3"><rect x="0.7" y="0.7" width="9" height="19.6"/><rect x="11.3" y="0.7" width="9" height="9"/><rect x="11.3" y="11.3" width="9" height="9"/></svg>
  </header>

  <div class="tile tile--sculp"><div class="tile__art" role="img" aria-label="Abstract stone sculpture photograph"></div><div class="tile__word">SCULP</div></div>
  <div class="tile tile--art"><div class="tile__art" role="img" aria-label="Geometric pastel illustration"></div><div class="tile__word">ART</div></div>
  <div class="tile tile--expressions"><div class="tile__word">EXPRESSIONS</div><div class="tile__art" role="img" aria-label="Black and white graphic portrait grid"></div></div>
  <div class="tile tile--oceania"><div class="tile__art" role="img" aria-label="Underwater photograph with a school of fish"></div><div class="tile__word">OCEANIA</div></div>
  <div class="tile tile--nature"><div class="tile__art" role="img" aria-label="Misty pine forest photograph"></div>
    <div class="tile__word title-light" style="top:47px;font-size:14px;color:#222">NATURE</div>
    <div class="tile__word title-bold" style="top:66px;font-size:14px;color:#222">BEHAVIOUR</div>
  </div>
  <div class="tile tile--phones"><div class="tile__art" role="img" aria-label="Scattered phone screens showing an editorial app"></div></div>
  <div class="tile tile--universe">
    <div class="abs" style="left:10px;top:10px;font-size:12px;line-height:12px">VELLORAN<br>UNIVERSE</div>
    <div class="abs" style="left:10px;top:48px;font-size:12px">Velloran + Marmotte</div>
  </div>
  <div class="abs fab">
    <svg width="18" height="22" viewBox="0 0 18 22" fill="none" stroke="#9a9a9a" stroke-width="1.3"><path d="M13 1l4 3-11 15-4 2 0-4z"/></svg>
  </div>
</section>

<!-- Article detail screen -->
<section class="screen screen--detail">
  <header class="appbar">
    <span class="appbar__label" style="left:19px;color:var(--ink)">EDIT</span>
    <svg class="abs" style="left:206px;top:15px" width="20" height="22" viewBox="0 0 20 22" fill="none" stroke="var(--icon)" stroke-width="1.3"><circle cx="15" cy="4" r="3"/><circle cx="4" cy="11" r="3"/><circle cx="15" cy="18" r="3"/><line x1="6.6" y1="9.6" x2="12.4" y2="5.4"/><line x1="6.6" y1="12.4" x2="12.4" y2="16.6"/></svg>
    <svg class="abs" style="left:258px;top:18px" width="20" height="15" viewBox="0 0 20 15" fill="none" stroke="var(--icon)" stroke-width="1.3"><rect x="0.7" y="0.7" width="18.6" height="13.6"/><path d="M1 1l9 7 9-7"/></svg>
    <svg class="abs" style="left:308px;top:15px" width="20" height="20" viewBox="0 0 20 20" fill="none" stroke="var(--icon)" stroke-width="1.3"><rect x="4" y="1" width="12" height="5"/><rect x="1" y="6" width="18" height="8"/><rect x="4" y="11" width="12" height="8"/><line x1="6" y1="14" x2="14" y2="14"/><line x1="6" y1="16.5" x2="14" y2="16.5"/></svg>
  </header>

  <div class="hero">
    <div class="hero__art" role="img" aria-label="Dense evergreen forest photograph"></div>
    <div class="abs title-light" style="left:0;width:100%;text-align:center;top:112px;font-size:31px;color:#fff;padding-left:.42em">NATURE</div>
    <div class="abs title-bold" style="left:0;width:100%;text-align:center;top:151px;font-size:32px;color:#fff">BEHAVIOUR</div>
  </div>

  <article class="article" role="img" aria-label="Faint misty forest backdrop behind the article text">
    <h2 class="article__heading">CREATION</h2>
    <div class="article__part">PART 1</div>
    <div class="article__body">
      <p>Lorem ipsum dolor sit amet, consectetur adipiscing elit. Vivamus quam elit, blandit at lacinia in, bibendum sed diam. Suspendisse eu sem et quam iaculis mollis malesuada ac leo. Aliquam est nibh, posuere interdum turpis vel, porttitor posuere justo. Mauris id turpis efficitur, dapibus tellus et, pharetra urna. Nullam finibus vitae mauris nec ullamcorper. Sed at erat eros. Curabitur elit odio, venenatis et leo sit amet, lobortis vehicula eros.</p>
      <p>In at neque tortor. Nullam urna urna, accumsan vitae tellus sit amet, tristique maximus tellus. Vivamus vestibulum arcu purus, nec laoreet felis imperdiet a. Suspendisse eget tellus non dui pretium aliquet quis finibus risus. Suspendisse ut eros tristique, blandit risus vitae, viverra ex. Cras</p>
    </div>
  </article>
</section>

</body>
</html>
```